business card design for luxurious real estate brand

using the attached logo, i am looking for a 2-sided business card design. the back should be the gold logo on black background. the front needs to include: gold logo, name, phone, email, and website

Industry/Entity Type

real estate

Contact Information for Business Card

logo, name, email, phone, website

Font styles to use
Sans Serif

```html
<!DOCTYPE html>
<html lang="en">
<head>
<meta charset="UTF-8">
<title>Maison Alder – Business Card</title>
<link rel="stylesheet" href="https://fonts.googleapis.com/css2?family=Montserrat:wght@400;500;600&display=swap">
<style>
  :root {
    --page-bg: #3a3a3b;
    --card-bg: #221f20;
    --card-sheen: #2c2a2b;
    --gold: #c9a24d;
    --text-light: #f2f0ec;
  }
  * { margin: 0; padding: 0; box-sizing: border-box; }
  html, body {
    width: 1200px;
    height: 1200px;
    overflow: hidden;
    background: var(--page-bg);
    font-family: "Montserrat", sans-serif;
  }
  .sheet {
    width: 1200px;
    height: 1200px;
    display: flex;
    flex-direction: column;
    align-items: center;
    justify-content: center;
    gap: 56px;
  }
  .card {
    width: 860px;
    height: 491px;
    border-radius: 36px;
    background: linear-gradient(100deg, var(--card-bg) 0%, var(--card-bg) 45%, var(--card-sheen) 55%, var(--card-bg) 75%);
    position: relative;
    box-shadow: 0 10px 30px rgba(0,0,0,0.45);
  }
  .brand {
    display: flex;
    align-items: center;
    gap: 18px;
    color: var(--gold);
    font-weight: 500;
    text-transform: uppercase;
    letter-spacing: 0.18em;
  }
  .brand-square {
    width: 22px;
    height: 22px;
    background: var(--gold);
    flex: none;
  }

  /* Front */
  .card-front .brand {
    position: absolute;
    left: 90px;
    top: 50%;
    transform: translateY(-50%);
    font-size: 30px;
  }
  .contact-block {
    position: absolute;
    left: 470px;
    top: 150px;
    color: var(--text-light);
  }
  .contact-name {
    color: var(--gold);
    font-weight: 600;
    font-size: 34px;
    letter-spacing: 0.02em;
    line-height: 1;
  }
  .contact-position {
    font-size: 17px;
    letter-spacing: 0.04em;
    margin-top: 6px;
  }
  .contact-list {
    list-style: none;
    margin-top: 26px;
    font-size: 19px;
  }
  .contact-list li {
    display: flex;
    align-items: center;
    gap: 12px;
    margin-bottom: 10px;
  }
  .contact-icon {
    width: 20px;
    height: 20px;
    flex: none;
    fill: none;
    stroke: var(--gold);
    stroke-width: 1.8;
    stroke-linecap: round;
    stroke-linejoin: round;
  }

  /* Back */
  .card-back {
    display: flex;
    align-items: center;
    justify-content: center;
  }
  .card-back .brand {
    font-size: 48px;
    gap: 26px;
  }
  .card-back .brand-square {
    width: 34px;
    height: 34px;
  }
</style>
</head>
<body>
  <main class="sheet">
    <section class="card card-front" aria-label="Card front">
      <div class="brand">
        <span class="brand-square"></span>
        <span class="brand-name">Maison Alder</span>
      </div>
      <div class="contact-block">
        <p class="contact-name">FULL NAME</p>
        <p class="contact-position">POSITION</p>
        <ul class="contact-list">
          <li>
            <svg class="contact-icon" viewBox="0 0 24 24"><path d="M5 3h4l2 5-2.5 1.5a11 11 0 0 0 6 6L16 13l5 2v4a2 2 0 0 1-2 2A16 16 0 0 1 3 5a2 2 0 0 1 2-2z"/></svg>
            <span>(000) 000 0000</span>
          </li>
          <li>
            <svg class="contact-icon" viewBox="0 0 24 24"><rect x="3" y="5" width="18" height="14" rx="1"/><path d="M3 6l9 7 9-7"/></svg>
            <span>email@company.com</span>
          </li>
          <li>
            <svg class="contact-icon" viewBox="0 0 24 24"><circle cx="12" cy="12" r="9"/><path d="M3 12h18M12 3c3 3 3 15 0 18M12 3c-3 3-3 15 0 18"/></svg>
            <span>www.company.com</span>
          </li>
        </ul>
      </div>
    </section>

    <section class="card card-back" aria-label="Card back">
      <div class="brand">
        <span class="brand-square"></span>
        <span class="brand-name">Maison Alder</span>
      </div>
    </section>
  </main>
</body>
</html>
```